Brenvick Holdings LLC, new Business cards

I'm moving offices and need new cards. Plus I'm open to modifying the current design of my card. I will keep the logo but would like to explore other layouts and fonts for the design. I've included the current double sided card for reference. I Like the navy color and white. Might be open to grays or silver. Needs to be clean and elegant.

Target Market(s)

Investors, buyers & sellers of private equities and real estate.

Contact Information for Business Card

Brenvick Holdings
Dorian P.K. Halvers, Managing Principal
418 Ostrander Ave., Suite 612
Denver, CO 80319
M: 970-555-0147, O: 303-555-0192
Dorian@brenvickholdings.example
Brenvickholdings.example

Colors
0354a2
ffffff
c4c4c4

Requirements
Must have
• Business card details.
• Logo raised or embossed, it was designed after a wax seal. Current has raised ink.
Nice to have
• Space on card to write additional notes.

```html
<!DOCTYPE html>
<html lang="en">
<head>
<meta charset="utf-8">
<title>Brenvick Holdings – Business Card</title>
<link href="https://fonts.googleapis.com/css2?family=Lato:wght@400;700&display=swap" rel="stylesheet">
<style>
  :root {
    --navy: #2b2550;
    --ink: #2f2b45;
    --white: #ffffff;
    --silver: #c8c8c8;
    --silver-light: #d8d8d8;
    --silver-dark: #bdbdbd;
    --rule: #d6d6d6;
    --backdrop: #3a3a3c;
  }
  * { box-sizing: border-box; margin: 0; padding: 0; }
  html, body {
    width: 1200px; height: 782px; overflow: hidden;
    background: var(--backdrop);
    font-family: "Lato", sans-serif;
  }
  .sheet {
    width: 1200px; height: 782px;
    display: flex; align-items: center; justify-content: center; gap: 40px;
  }
  .card {
    width: 540px; height: 309px;
    border-bottom: 5px solid var(--navy);
    position: relative;
    box-shadow: 0 10px 24px rgba(0,0,0,.35);
    flex: none;
  }
  .card--front {
    background: var(--white);
    display: flex; align-items: center;
  }
  .brand {
    width: 42%; height: 100%;
    display: flex; align-items: center; justify-content: center; gap: 9px;
    color: var(--navy);
    padding: 0 12px;
  }
  .brand__dot { width: 18px; height: 18px; border-radius: 50%; background: var(--navy); flex: none; }
  .brand__name {
    font-size: 16px; font-weight: 700; letter-spacing: .06em;
    text-transform: uppercase; white-space: nowrap;
  }
  .divider { width: 1px; height: 130px; background: var(--rule); flex: none; }
  .details { padding-left: 24px; color: var(--ink); font-size: 14px; line-height: 1.32; white-space: nowrap; }
  .details__name { color: var(--navy); font-size: 18px; font-weight: 700; text-transform: uppercase; letter-spacing: .02em; }
  .details__title { margin-bottom: 2px; }
  .details__line { display: flex; align-items: center; gap: 6px; }
  .details__line svg { width: 12px; height: 12px; fill: var(--navy); flex: none; }
  .details__label { font-weight: 700; }
  .card--back {
    background:
      radial-gradient(circle at 30% 35%, var(--silver-light) 0%, transparent 55%),
      radial-gradient(circle at 75% 70%, var(--silver-light) 0%, transparent 50%),
      linear-gradient(135deg, var(--silver) 0%, var(--silver-dark) 100%);
  }
</style>
</head>
<body>
<main class="sheet">
  <section class="card card--front" aria-label="Card front">
    <div class="brand">
      <span class="brand__dot"></span>
      <span class="brand__name">Brenvick Holdings</span>
    </div>
    <div class="divider"></div>
    <div class="details">
      <div class="details__name">Dorian P.K. Halvers</div>
      <div class="details__title">Managing Principal</div>
      <div class="details__line">
        <svg viewBox="0 0 24 24"><path d="M6.6 10.8a15 15 0 0 0 6.6 6.6l2.2-2.2c.3-.3.7-.4 1-.2 1.1.4 2.3.6 3.6.6.6 0 1 .4 1 1V20c0 .6-.4 1-1 1A17 17 0 0 1 3 4c0-.6.4-1 1-1h3.5c.6 0 1 .4 1 1 0 1.3.2 2.5.6 3.6.1.3 0 .7-.2 1z"/></svg>
        <span>970-555-0147 | <span class="details__label">O:</span> 303-555-0192</span>
      </div>
      <div class="details__line">
        <svg viewBox="0 0 24 24"><path d="M2 5h20v14H2zm2 2v.5l8 5 8-5V7zm0 2.8V17h16V9.8l-8 5z"/></svg>
        <span>Dorian@brenvickholdings.example</span>
      </div>
      <div class="details__line">
        <svg viewBox="0 0 24 24"><path d="M12 2a10 10 0 1 0 0 20 10 10 0 0 0 0-20zm6.9 9h-3a15 15 0 0 0-1.3-5.6A8 8 0 0 1 18.9 11zM12 4.1c.9 1.3 1.7 3.7 1.9 6.9h-3.8c.2-3.2 1-5.6 1.9-6.9zM9.4 5.4A15 15 0 0 0 8.1 11h-3a8 8 0 0 1 4.3-5.6zM5.1 13h3a15 15 0 0 0 1.3 5.6A8 8 0 0 1 5.1 13zm6.9 6.9c-.9-1.3-1.7-3.7-1.9-6.9h3.8c-.2 3.2-1 5.6-1.9 6.9zm2.6-1.3a15 15 0 0 0 1.3-5.6h3a8 8 0 0 1-4.3 5.6z"/></svg>
        <span>www.Brenvickholdings.example</span>
      </div>
      <div>418 Ostrander Ave., Suite 612</div>
      <div>Denver, CO 80319</div>
    </div>
  </section>
  <section class="card card--back" role="img" aria-label="Card back: repeating pattern of the embossed wax-seal logo in light grey on silver grey"></section>
</main>
</body>
</html>
```